IT services company needs a business card designed

-2 sided business card.-Front is going to be the logo raised (3D floating effect) on a black background. Make the logos spider web shiny silver and keep the spider the same design. -Back needs to have the following information:Doug Farrow, Managing Partner, Cell: 602-488-3179, Website: Kolvantra.com, Email: Doug@Kolvantra.com
Target Market(s)
IT Services
Industry/Entity Type
It Company
Contact Information for Business Card
-2 sided business card.
-Front is going to be the logo raised (3D floating effect) on a black background. Make the logos spider web shiny silver and keep the spider the same design.
-Back needs to have the following information:
Doug Farrow, Managing Partner, Cell: 602-488-3179, Website: Kolvantra.com, Email: Doug@Kolvantra.com
Look and feel

```html
<!DOCTYPE html>
<html lang="en">
<head>
<meta charset="utf-8">
<title>Kolvantra Business Card</title>
<link href="https://fonts.googleapis.com/css2?family=Questrial&display=swap" rel="stylesheet">
<style>
  :root {
    --page-bg: #dcdcdc;
    --card-bg: #e6e8f0;
    --card-bg-front: #e2e4ec;
    --brand-blue: #2f6fdc;
    --band-blue: #4a8be0;
    --ink: #141418;
    --web-gray: rgba(138,141,148,0.4);
    --web-blue: rgba(142,192,234,0.55);
    --spider-soft: rgba(142,192,234,0.45);
  }
  * { box-sizing: border-box; margin: 0; padding: 0; }
  html, body { width: 1200px; height: 1200px; overflow: hidden; }
  body {
    background: var(--page-bg);
    font-family: "Questrial", sans-serif;
    color: var(--ink);
    position: relative;
  }
  .card {
    position: absolute;
    left: 250px;
    width: 700px;
    height: 400px;
    overflow: hidden;
    box-shadow: 0 6px 18px rgba(0,0,0,0.18);
  }
  .card-back { top: 130px; background: var(--card-bg); }
  .card-front { top: 650px; background: var(--card-bg-front); }

  .top-band { position: absolute; top: 0; left: 0; width: 700px; height: 42px; }

  .brand-mark {
    position: absolute;
    display: flex;
    align-items: center;
    gap: 10px;
    letter-spacing: 2px;
    color: var(--ink);
    white-space: nowrap;
  }
  .brand-mark .dot {
    width: 14px; height: 14px; border-radius: 50%;
    background: var(--brand-blue);
  }
  .card-back .brand-mark { left: 56px; top: 118px; font-size: 24px; }

  .identity { position: absolute; right: 110px; top: 82px; white-space: nowrap; }
  .identity .person-name { font-size: 40px; line-height: 1; }
  .identity .person-title { font-size: 22px; margin-top: 6px; }

  .spider-illustration {
    position: absolute;
    right: -40px; top: 100px;
    width: 400px; height: 340px;
    background: radial-gradient(closest-side at 50% 50%, var(--spider-soft), rgba(142,192,234,0.12) 70%, transparent 100%);
  }

  .contact-list { position: absolute; left: 0; top: 220px; width: 520px; }
  .contact-row { position: relative; height: 60px; }
  .contact-row svg.trace { position: absolute; left: 0; top: 0; }
  .contact-icon {
    position: absolute; left: 270px; top: 22px;
    width: 36px; height: 36px; border-radius: 50%;
    background: var(--brand-blue);
    display: flex; align-items: center; justify-content: center;
  }
  .contact-text { position: absolute; left: 324px; top: 28px; font-size: 17px; white-space: nowrap; }

  .web-corner-gray {
    position: absolute; left: -20px; top: -20px; width: 320px; height: 240px;
    background: radial-gradient(closest-side at 50% 50%, var(--web-gray), transparent 100%);
  }
  .web-corner-blue {
    position: absolute; right: -40px; bottom: -40px; width: 280px; height: 240px;
    background: radial-gradient(closest-side at 50% 50%, var(--web-blue), transparent 100%);
  }
  .card-front .brand-mark {
    left: 0; right: 0; top: 170px; justify-content: center;
    font-size: 52px; letter-spacing: 4px;
  }
  .card-front .brand-mark .dot { width: 22px; height: 22px; }
</style>
</head>
<body>

<section class="card card-back" aria-label="Business card back">
  <svg class="top-band" viewBox="0 0 700 42" aria-hidden="true">
    <polygon points="0,26 0,34 300,24 420,24 700,22 700,0 400,12" fill="var(--band-blue)"/>
  </svg>

  <div class="spider-illustration" role="img" aria-label="Faint low-poly spider on a circuit-style web"></div>

  <div class="brand-mark"><span class="dot"></span><span>KOLVANTRA</span></div>

  <div class="identity">
    <div class="person-name">Doug Farrow</div>
    <div class="person-title">Managing Partner</div>
  </div>

  <div class="contact-list">
    <div class="contact-row">
      <svg class="trace" width="280" height="60" aria-hidden="true"><polyline points="0,22 90,22 120,40 272,40" fill="none" stroke="var(--brand-blue)" stroke-width="3"/></svg>
      <span class="contact-icon"><svg width="18" height="18" viewBox="0 0 24 24"><path d="M6.6 10.8a15 15 0 0 0 6.6 6.6l2.2-2.2a1 1 0 0 1 1-.25 11 11 0 0 0 3.6.6 1 1 0 0 1 1 1V20a1 1 0 0 1-1 1A17 17 0 0 1 3 4a1 1 0 0 1 1-1h3.5a1 1 0 0 1 1 1 11 11 0 0 0 .6 3.6 1 1 0 0 1-.25 1z" fill="#fff"/></svg></span>
      <span class="contact-text">602-488-3179</span>
    </div>
    <div class="contact-row">
      <svg class="trace" width="280" height="60" aria-hidden="true"><polyline points="0,22 90,22 120,40 272,40" fill="none" stroke="var(--brand-blue)" stroke-width="3"/></svg>
      <span class="contact-icon"><svg width="18" height="18" viewBox="0 0 24 24"><rect x="3" y="6" width="18" height="12" fill="#fff"/><polyline points="3,6 12,13 21,6" fill="none" stroke="var(--brand-blue)" stroke-width="1.5"/></svg></span>
      <span class="contact-text">Doug@Kolvantra.com</span>
    </div>
    <div class="contact-row">
      <svg class="trace" width="280" height="60" aria-hidden="true"><polyline points="0,22 90,22 120,40 272,40" fill="none" stroke="var(--brand-blue)" stroke-width="3"/></svg>
      <span class="contact-icon"><svg width="20" height="20" viewBox="0 0 24 24" fill="none" stroke="#fff" stroke-width="1.6"><circle cx="12" cy="12" r="9"/><ellipse cx="12" cy="12" rx="4" ry="9"/><line x1="3" y1="12" x2="21" y2="12"/><line x1="5" y1="7" x2="19" y2="7"/><line x1="5" y1="17" x2="19" y2="17"/></svg></span>
      <span class="contact-text">www.Kolvantra.com</span>
    </div>
  </div>
</section>

<section class="card card-front" aria-label="Business card front">
  <div class="web-corner-gray" role="img" aria-label="Gray circuit-style spider web corner decoration"></div>
  <div class="web-corner-blue" role="img" aria-label="Blue circuit-style spider web corner decoration"></div>
  <div class="brand-mark"><span class="dot"></span><span>KOLVANTRA</span></div>
</section>

</body>
</html>
```